Header and footer for report

We would like a header and footer for our building management reports that incorporate a modern city skyline and our logo.

As well as update our other stationery.

```html
<!DOCTYPE html>
<html lang="en">
<head>
<meta charset="utf-8">
<title>Spire Bay – Stationery Set</title>
<link href="https://fonts.googleapis.com/css2?family=Roboto:wght@400;500;700&display=swap" rel="stylesheet">
<style>
  :root {
    --backdrop: #d4d4d4;
    --paper: #f3f3f3;
    --brand-blue: #1b5ea6;
    --brand-blue-deep: #175595;
    --ink: #1a1a1a;
    --text-grey: #4a4a4a;
    --skyline-pale: #e4e4e4;
    --skyline-mid: #c9c9c9;
    --skyline-blue-light: #3473b8;
    --window-grey: #5a5a5a;
  }
  * { box-sizing: border-box; margin: 0; padding: 0; }
  html, body { width: 1200px; height: 580px; overflow: hidden; }
  body {
    background: var(--backdrop);
    font-family: "Roboto", Arial, sans-serif;
    color: var(--ink);
    position: relative;
  }
  .sheet { position: absolute; overflow: hidden; background: var(--paper); box-shadow: 0 6px 14px rgba(0,0,0,.18); }
  .brand-name { font-weight: 700; color: var(--brand-blue); letter-spacing: .02em; white-space: nowrap; }
  .brand-name.on-blue { color: #fff; }

  /* city skyline artwork areas: soft gradient in the artwork's tones */
  .skyline-art {
    position: absolute;
    background: linear-gradient(180deg, rgba(228,228,228,0) 0%, var(--skyline-pale) 22%, var(--skyline-mid) 78%, #dedede 100%);
  }
  .skyline-art.on-blue {
    background: linear-gradient(180deg, rgba(27,94,166,0) 0%, #2062aa 30%, var(--skyline-blue-light) 80%, #2c6bb1 100%);
  }

  .contact-list { position: absolute; list-style: none; color: var(--text-grey); }
  .contact-list li { display: flex; align-items: flex-start; }
  .contact-list svg { flex: none; fill: var(--brand-blue); }

  /* business card front */
  .card-front { left: 135px; top: 96px; width: 124px; height: 71px; }
  .card-front .brand-name { position: absolute; left: 7px; top: 21px; font-size: 4.6px; }
  .card-front .card-web { position: absolute; right: 6px; top: 5px; font-size: 2.2px; color: var(--text-grey); }
  .card-front .person { position: absolute; left: 7px; top: 37px; font-size: 5px; color: var(--ink); }
  .card-front .person b { color: var(--brand-blue); font-weight: 700; }
  .card-front .role { position: absolute; left: 7px; top: 43px; font-size: 2.8px; color: var(--text-grey); }
  .card-front .contact-list { left: 7px; top: 50px; font-size: 2.1px; line-height: 2.9px; }
  .card-front .contact-list svg { width: 2.2px; height: 2.2px; margin: .3px 2px 0 0; }
  .card-front .skyline-art { left: 50px; top: 28px; width: 74px; height: 43px; }

  /* business card back */
  .card-back { left: 278px; top: 96px; width: 124px; height: 71px; background: linear-gradient(160deg, #2a72bd, var(--brand-blue-deep)); }
  .card-back .skyline-art { left: 0; top: 40px; width: 124px; height: 31px; opacity: .6; }
  .card-back .brand-name { position: absolute; left: 0; right: 0; top: 46px; text-align: center; font-size: 9px; }
  .card-back .card-web { position: absolute; left: 0; right: 0; top: 58px; text-align: center; font-size: 3px; color: #fff; }

  /* envelope front */
  .envelope-front { left: 135px; top: 187px; width: 267px; height: 133px; }
  .envelope-front .brand-name { position: absolute; left: 8px; top: 41px; font-size: 10px; }
  .envelope-front .contact-list { left: 9px; top: 61px; font-size: 3.8px; line-height: 5.6px; }
  .envelope-front .contact-list svg { width: 3.6px; height: 3.6px; margin: .6px 3px 0 0; }
  .envelope-front .skyline-art { left: 110px; top: 4px; width: 157px; height: 114px; }
  .envelope-front .address-window { position: absolute; left: 191px; top: 80px; width: 66px; height: 27px; background: var(--window-grey); border-radius: 2px; }
  .footer-band { position: absolute; left: 0; right: 0; bottom: 0; }
  .footer-band svg { display: block; }
  .footer-band .band-web { position: absolute; right: 10px; bottom: 3.5px; font-size: 5.5px; color: #fff; display: flex; align-items: center; gap: 3px; }

  /* envelope back */
  .envelope-back { left: 135px; top: 343px; width: 267px; height: 132px; }
  .envelope-back .flap { position: absolute; left: 0; top: 0; }
  .envelope-back .brand-name { position: absolute; left: 0; right: 0; top: 29px; text-align: center; font-size: 8px; }
  .envelope-back .skyline-art { left: 0; top: 60px; width: 267px; height: 68px; opacity: .75; }
  .envelope-back .base-line { position: absolute; left: 0; right: 0; bottom: 0; height: 4px; background: var(--ink); }

  /* letterhead */
  .letterhead { left: 436px; top: 96px; width: 269px; height: 379px; }
  .letterhead .brand-name.main { position: absolute; left: 11px; top: 52px; font-size: 13px; }
  .letterhead .corner-brand { position: absolute; right: 15px; top: 10px; text-align: right; font-size: 8px; line-height: 8.5px; font-weight: 700; color: var(--brand-blue); }
  .letterhead .corner-brand span { display: block; }
  .letterhead .corner-brand .light { font-weight: 400; color: var(--ink); font-size: 7px; }
  .letterhead .corner-bar { position: absolute; right: 0; top: 10px; width: 7px; height: 16px; border-left: 3px solid var(--brand-blue-deep); border-right: 2px solid var(--brand-blue-deep); }
  .letterhead .salutation { position: absolute; left: 11px; top: 99px; font-size: 6.5px; color: var(--ink); }
  .letterhead .salutation b { color: var(--brand-blue); font-weight: 700; }
  .letterhead .letter-body { position: absolute; left: 11px; top: 117px; width: 248px; font-size: 3.9px; line-height: 6.3px; color: var(--text-grey); }
  .letterhead .letter-body p + p { margin-top: 6px; }
  .letterhead .skyline-art { left: 0; top: 230px; width: 269px; height: 140px; }
  .letterhead .signer { position: absolute; left: 10px; top: 234px; font-size: 8.5px; color: var(--brand-blue); font-weight: 500; }
  .letterhead .signer-role { position: absolute; left: 10px; top: 244px; font-size: 5px; color: var(--ink); font-weight: 500; letter-spacing: .03em; }
  .letterhead .contact-list { left: 11px; top: 327px; font-size: 5.5px; line-height: 8.4px; color: var(--ink); }
  .letterhead .contact-list svg { width: 5px; height: 5px; margin: 1.5px 5px 0 0; }
  .letterhead .band-web { font-size: 7px; bottom: 3px; right: 14px; }

  /* folder */
  .folder { left: 740px; top: 95px; width: 269px; height: 380px; background: var(--brand-blue-deep); }
  .folder .brand-name { position: absolute; left: 0; right: 0; top: 100px; text-align: center; font-size: 24px; }
  .folder .skyline-art { left: 0; top: 235px; width: 269px; height: 142px; }
  .folder .corner-line { position: absolute; bottom: 0; height: 3px; width: 52px; background: var(--ink); }
  .folder .corner-line.left { left: 0; }
  .folder .corner-line.right { right: 0; }
</style>
</head>
<body>

<!-- Business card, front -->
<section class="sheet card-front">
  <div class="skyline-art" role="img" aria-label="Light grey modern city skyline artwork"></div>
  <div class="card-web">www.spirebay.com</div>
  <div class="brand-name">SPIRE BAY</div>
  <div class="person">ADA <b>VOSS</b></div>
  <div class="role">CEO &amp; FOUNDER</div>
  <ul class="contact-list">
    <li><svg viewBox="0 0 10 10"><path d="M5 0a3.6 3.6 0 0 0-3.6 3.6C1.4 6.4 5 10 5 10s3.6-3.6 3.6-6.4A3.6 3.6 0 0 0 5 0z"/></svg>your address here, state</li>
    <li><svg viewBox="0 0 10 10"><path d="M2 0l2 2.5-1 1.3a6 6 0 0 0 3.2 3.2l1.3-1L10 8l-1.5 2C4 10 0 6 0 1.5z"/></svg>+000 555 0142</li>
    <li><svg viewBox="0 0 10 10"><path d="M0 2h10v6H0z"/></svg>hi@spirebay.co</li>
  </ul>
</section>

<!-- Business card, back -->
<section class="sheet card-back">
  <div class="skyline-art on-blue" role="img" aria-label="Faint blue city skyline artwork"></div>
  <div class="brand-name on-blue">SPIRE BAY</div>
  <div class="card-web">www.spirebay.com</div>
</section>

<!-- Envelope, front -->
<section class="sheet envelope-front">
  <div class="skyline-art" role="img" aria-label="Light grey modern city skyline artwork"></div>
  <div class="address-window"></div>
  <div class="brand-name">SPIRE BAY</div>
  <ul class="contact-list">
    <li><svg viewBox="0 0 10 10"><path d="M5 0a3.6 3.6 0 0 0-3.6 3.6C1.4 6.4 5 10 5 10s3.6-3.6 3.6-6.4A3.6 3.6 0 0 0 5 0zm0 5a1.4 1.4 0 1 1 0-2.8A1.4 1.4 0 0 1 5 5z"/></svg><span>your address here, state,<br>zip code 0004</span></li>
    <li><svg viewBox="0 0 10 10"><path d="M2 0l2 2.5-1 1.3a6 6 0 0 0 3.2 3.2l1.3-1L10 8l-1.5 2C4 10 0 6 0 1.5z"/></svg>+000 555 0142</li>
    <li><svg viewBox="0 0 10 10"><path d="M0 2h10v6H0z"/></svg>hi@spirebay.co</li>
    <li><svg viewBox="0 0 10 10"></svg>www.spirebay.com</li>
  </ul>
  <div class="footer-band">
    <svg width="267" height="15" viewBox="0 0 267 15"><polygon points="190,0 267,0 267,15 186,15" fill="#1b5ea6"/><rect x="0" y="11.5" width="190" height="3.5" fill="#1a1a1a"/></svg>
    <div class="band-web"><svg width="5" height="5" viewBox="0 0 10 10"><circle cx="5" cy="5" r="4.2" fill="none" stroke="#fff" stroke-width="1.2"/><path d="M1 5h8M5 1v8" stroke="#fff" stroke-width="1"/></svg>www.spirebay.com</div>
  </div>
</section>

<!-- Envelope, back -->
<section class="sheet envelope-back">
  <div class="skyline-art" role="img" aria-label="Faint grey city skyline artwork"></div>
  <svg class="flap" width="267" height="41" viewBox="0 0 267 41"><polygon points="0,0 267,0 250,41 17,41" fill="#1b5ea6"/></svg>
  <div class="brand-name on-blue">SPIRE BAY</div>
  <div class="base-line"></div>
</section>

<!-- Letterhead -->
<section class="sheet letterhead">
  <div class="skyline-art" role="img" aria-label="Modern city skyline artwork in light grey"></div>
  <div class="corner-brand"><span>SPIRE</span><span class="light">BAY</span></div>
  <div class="corner-bar"></div>
  <div class="brand-name main">SPIRE BAY</div>
  <p class="salutation">Dear <b>Mr Lane,</b></p>
  <div class="letter-body">
    <p>Contrary to popular belief, Lorem Ipsum is not simply random text. It has roots in a piece of classical Latin literature from 45 BC, making it over 2000 years old. A Latin professor looked up one of the more obscure Latin words, consectetur, from a Lorem Ipsum passage, and going through the cites of the word in classical literature, discovered the undoubtable source. This book is a treatise on the theory of ethics, very popular during the Renaissance. The first line of Lorem Ipsum comes from a line in section 1.10.32.</p>
    <p>The standard chunk of Lorem Ipsum used since the 1500s is reproduced below for those interested. Sections 1.10.32 and 1.10.33 are also reproduced in their exact original form, accompanied by English versions from a later translation.</p>
    <p>There are many variations of passages of Lorem Ipsum available, but the majority have suffered alteration in some form, by injected humour, or randomised words which don't look even slightly believable. If you are going to use a passage of Lorem Ipsum, you need to be sure there isn't anything embarrassing hidden in the middle of text. All the Lorem Ipsum generators on the Internet tend to repeat predefined chunks as necessary, making this the first true generator on the Internet. It uses a dictionary of over 200 Latin words, combined with a handful of model sentence structures, to generate Lorem Ipsum which looks reasonable. The generated Lorem Ipsum is therefore always free from repetition, injected humour, or non-characteristic words etc.</p>
  </div>
  <div class="signer">Tom Reyes</div>
  <div class="signer-role">CEO &amp; FOUNDER</div>
  <ul class="contact-list">
    <li><svg viewBox="0 0 10 10"><path d="M5 0a3.6 3.6 0 0 0-3.6 3.6C1.4 6.4 5 10 5 10s3.6-3.6 3.6-6.4A3.6 3.6 0 0 0 5 0zm0 5a1.4 1.4 0 1 1 0-2.8A1.4 1.4 0 0 1 5 5z"/></svg><span>your address here, state,<br>zip code 0004</span></li>
    <li><svg viewBox="0 0 10 10"><path d="M2 0l2 2.5-1 1.3a6 6 0 0 0 3.2 3.2l1.3-1L10 8l-1.5 2C4 10 0 6 0 1.5z"/></svg>+000 555 0142</li>
    <li><svg viewBox="0 0 10 10"><path d="M0 2h10v6H0z"/></svg>hi@spirebay.co</li>
    <li><svg viewBox="0 0 10 10"><circle cx="5" cy="5" r="4.2" fill="none" stroke="#1b5ea6" stroke-width="1.2"/><path d="M1 5h8M5 1v8" stroke="#1b5ea6" stroke-width="1"/></svg>www.spirebay.com</li>
  </ul>
  <div class="footer-band">
    <svg width="269" height="17" viewBox="0 0 269 17"><polygon points="170,0 269,0 269,17 164,17" fill="#1b5ea6"/><rect x="0" y="13" width="168" height="4" fill="#1a1a1a"/></svg>
    <div class="band-web">www.spirebay.com</div>
  </div>
</section>

<!-- Presentation folder -->
<section class="sheet folder">
  <div class="skyline-art on-blue" role="img" aria-label="Faint blue city skyline artwork"></div>
  <div class="brand-name on-blue">SPIRE BAY</div>
  <div class="corner-line left"></div>
  <div class="corner-line right"></div>
</section>

</body>
</html>
```